Commercial Cleaning Company Website Design

We are working with Harbor Tidy Squad. They are a commercial cleaning company that needs a new website design.

Some sites to use for inspiration:

https://www.velmoxa.com
https://glint-panewashing.com
https://tidykelps.net
https://warmnestdwell.com
https://www.thescrubbingcouncil.com
https://www.pennybroom.com

Thank you for taking the time to consider designing a website for us. We are web developers based in Stockton and Los Angeles, CA, USA. Most of our projects go through the same process. Understanding this process may help you win a project with us. We custom-code all of our websites in-house. We don’t have any requirements as to what tools you use for your design, but we prefer Figma files. For any design that we label as four-stars, we send it to the client for review. The client picks the final design they want us to use. Once we complete this process, we will continue to show additional clients all the four-star sites and purchase them later. Your designs will have multiple chances to sell. For better chances of success, we ask that you follow these guidelines.

IMAGES:
If you use any images or icons in the design, we ask that you have a link to the asset so we can purchase the image/icon. Most of the designs we submit do not have the customer’s images on them unless they have some great images. Be creative; show us the feeling you are trying to portray with your image choices. Use any royalty-free site you choose. We subscribe to Vorlan and mainly use their images, but we can purchase images outside of Vorlan.

PLEASE NOTE: we will not submit designs to clients with watermarks on the images.

FONTS:
We ask that you identify the fonts used in the design. This can be done in a message if you want. We typically use Google Fonts and Vorlan Fonts.

CONTENT:
We're always open to different content and ideas. We often submit designs with stock images so the client can see our vision. We typically take pictures after the website launch to use their images with our vision. Lorem Ipsum is fine for paragraphs, but we ask that you write the headers in correct English. We want to be able to show the vision and identify the sections of the website.

INSPIRATION:
We typically add a couple of links in the brief of websites we like to help you get started in your design.

REVISIONS:
We do not often ask for revisions of the designs unless we see something in the design that may not appeal to the client. If there are slight changes that we want to make, we do that in the development process.

FEEDBACK:
We rarely give feedback on designs during the design process. We are working on many website projects and do not have the time to provide feedback. We usually respond if your request is well thought out and asks specific questions, but a note asking “feedback, please” usually goes unanswered.

```html
<!DOCTYPE html>
<html lang="en">
<head>
<meta charset="utf-8">
<title>Harbor Tidy Squad — Commercial Cleaning</title>
<link href="https://fonts.googleapis.com/css2?family=Poppins:wght@300;400;500;600;700;800&display=swap" rel="stylesheet">
<style>
:root{
  --blue:#1d4ab8;
  --blue-deep:#1a47b8;
  --red:#e3251d;
  --yellow:#ffad00;
  --ink:#2b2b2b;
  --muted:#6b6b6b;
  --line:#d9d9d9;
  --sky:#e4f5fd;
  --white:#fff;
}
*{box-sizing:border-box;margin:0;padding:0}
html,body{width:1200px;height:4252px;overflow:hidden}
body{position:relative;font-family:"Poppins",sans-serif;color:var(--ink);background:var(--white)}
.abs{position:absolute}
.topbar{left:0;top:0;width:1200px;height:37px;background:var(--blue-deep);color:#fff;font-size:11px;font-weight:500}
.topbar .contact{left:88px;top:11px;display:flex;gap:26px}
.topbar .socials{left:812px;top:11px;display:flex;gap:16px;align-items:center}
.topbar .socials span{width:13px;height:13px;border-radius:50%;background:rgba(255,255,255,.85);display:block}
.quote-tab{left:935px;top:0;width:175px;height:37px;background:var(--red);color:#fff;font-size:11px;font-weight:700;text-align:center;line-height:37px}
.hero-bg{left:0;top:37px;width:1200px;height:700px;background:linear-gradient(180deg,var(--sky),#fff)}
.brand{display:flex;align-items:center;gap:12px;font-weight:600;color:var(--blue);letter-spacing:6px}
.brand .mark{width:22px;height:22px;border-radius:50%;background:var(--red);flex:none}
.header-brand{left:88px;top:74px;font-size:20px}
.nav{left:675px;top:82px;display:flex;gap:30px;font-size:11px;font-weight:500;color:#333}
.hero-title{left:0;top:148px;width:1200px;text-align:center;font-size:56px;line-height:58px;font-weight:800;color:var(--blue)}
.pill{display:inline-block;width:108px;height:48px;border-radius:26px;vertical-align:-4px;background:linear-gradient(90deg,#c9d3dc,#6f86a3,#d8dde2)}
.tagline{left:0;top:978px;width:1200px;text-align:center;font-size:24px;font-weight:300;line-height:40px;color:#555}
.section-title{font-size:36px;font-weight:700;color:var(--blue)}
.services-title{left:87px;top:1238px}
.services-text{left:87px;top:1292px;width:270px;font-size:13px;line-height:22px;color:var(--muted)}
.circle-btn{left:86px;top:1388px;width:70px;height:70px;border-radius:50%;background:var(--blue)}
.card{top:1127px;width:228px;height:381px;background:#fff;border-radius:16px;box-shadow:0 10px 30px rgba(0,0,0,.08);overflow:hidden}
.card .photo{height:190px}
.card h3{margin:24px 0 0 27px;font-size:14px;line-height:20px;font-weight:700;color:#333}
.card p{margin:12px 27px 0;font-size:11.5px;line-height:18px;color:var(--muted);height:36px}
.btn{display:inline-block;background:var(--red);color:#fff;font-weight:700;font-size:11px;border-radius:20px;text-align:center}
.card .btn{margin:14px 0 0 27px;width:108px;height:34px;line-height:34px}
.center{left:0;width:1200px;text-align:center}
.why-title{top:1612px}
.why-text{top:1668px;font-size:13px;line-height:22px;color:var(--muted)}
.why-list{left:596px;top:1762px;width:514px}
.why-item{font-size:12.5px;font-weight:700;color:#333;padding:10px 0 18px;border-bottom:1px solid var(--line)}
.why-item.plain{border-bottom:none}
.why-box{background:var(--blue);color:#fff;border-radius:10px;padding:18px 30px 20px;margin:12px 0 14px;box-shadow:0 8px 20px rgba(29,74,184,.25)}
.why-box h4{font-size:12.5px;font-weight:700;margin-bottom:12px}
.why-box p{font-size:11.5px;line-height:17px;font-weight:400}
.fleet{top:2265px;font-size:24px;line-height:40px;font-weight:300;color:#555}
.areas-title{left:87px;top:2456px}
.areas-text{left:87px;top:2516px;width:450px;font-size:13px;line-height:22px;color:var(--muted)}
.areas{left:140px;top:3050px;display:flex}
.areas ul{list-style:none;height:210px;padding:20px 0 0 38px;border-right:1px solid var(--line)}
.areas ul:last-child{border-right:none}
.areas li{display:flex;align-items:center;gap:9px;font-size:16px;color:#555;height:35.5px}
.quote-title{top:3350px}
.quote-text{top:3407px;font-size:13px;color:var(--muted)}
.footer-bg{left:0;top:3726px;width:1200px;height:526px;background:var(--blue-deep);border-top-right-radius:330px 300px}
.form{left:258px;top:3462px;width:684px;height:361px;background:var(--yellow);border-radius:40px}
.field{position:absolute}
.field label{display:block;font-size:10.5px;font-weight:700;color:#fff;margin-bottom:6px}
.field .input{background:#fff;border-radius:20px;height:39px;font-size:13px;color:#555;padding:11px 27px}
.field .area{border-radius:16px;height:128px}
.submit{left:285px;top:293px;width:115px;height:42px;line-height:42px}
.footer-brand{left:110px;top:3968px;font-size:27px;color:#fff}
.footer-brand .mark{width:24px;height:24px}
.fsocial{left:190px;top:4049px;display:flex;gap:11px}
.fsocial span{width:34px;height:34px;border-radius:50%;background:rgba(255,255,255,.2);display:block}
.fcol{color:#fff;font-size:12px;line-height:22px}
.fcol h5{font-size:16px;font-weight:600;margin-bottom:14px}
.fcol b{font-weight:700;font-size:11px}
.hours{display:grid;grid-template-columns:65px 120px}
.fline{left:87px;top:4194px;width:1026px;height:1px;background:rgba(255,255,255,.25)}
.copy{top:4218px;color:#fff;font-size:13px;font-weight:600}
.chat{left:1133px;top:4155px;width:44px;height:44px;border-radius:50%;background:var(--red);border:2px solid #fff}
</style>
</head>
<body>

<div class="abs topbar">
  <div class="abs contact">
    <span>&#9742; Phone: (555) 214-7730</span>
    <span>&#9993; Email: harbortidysquad.com</span>
  </div>
  <div class="abs socials" aria-label="Social links"><span></span><span></span><span></span></div>
</div>
<div class="abs quote-tab">REQUEST A QUOTE</div>

<div class="abs hero-bg"></div>
<div class="abs brand header-brand"><span class="mark"></span>HARBOR TIDY SQUAD</div>
<nav class="abs nav"><span>HOME</span><span>ABOUT US</span><span>SERVICES</span><span>TESTIMONIALS</span><span>CONTACT US</span></nav>

<h1 class="abs hero-title">PROFESSIONAL COMMERCIAL<br>CLEANING <span class="pill" role="img" aria-label="Cleaning team photo"></span> SERVICES YOU<br>CAN TRUST</h1>

<svg class="abs" style="left:87px;top:363px" width="1021" height="527" role="img" aria-label="Photo of two cleaners washing office windows">
  <defs><linearGradient id="g1" x1="0" y1="0" x2="1" y2="1"><stop offset="0" stop-color="#5a5f66"/><stop offset=".5" stop-color="#b9bcc0"/><stop offset="1" stop-color="#e9eaec"/></linearGradient></defs>
  <path fill="url(#g1)" d="M40,0 H981 A40,40 0 0 1 1021,40 V382 A40,40 0 0 1 981,422 H873 A40,40 0 0 0 833,462 V487 A40,40 0 0 1 793,527 H40 A40,40 0 0 1 0,487 V40 A40,40 0 0 1 40,0 Z"/>
</svg>

<p class="abs tagline">Reliable, efficient, and eco-friendly cleaning solutions for offices,<br>retail spaces, and commercial facilities across.</p>

<h2 class="abs section-title services-title">OUR SERVICES</h2>
<p class="abs services-text">We specialize in high pressure cleaning of trucks, trailers, buildings, underground parking garages</p>
<div class="abs circle-btn">
  <svg width="70" height="70"><path d="M29 41 L42 28 M32 28 H42 V38" stroke="#fff" stroke-width="2" fill="none"/></svg>
</div>

<div class="abs card" style="left:400px">
  <div class="photo" role="img" aria-label="Cleaner wiping an office desk" style="background:linear-gradient(135deg,#9fb8c4,#6f8e9b)"></div>
  <h3>OFFICE &amp; COMMERCIAL<br>CLEANING</h3>
  <p>Daily, weekly, or customized cleaning schedules.</p>
  <span class="btn">VIEW MORE</span>
</div>
<div class="abs card" style="left:645px">
  <div class="photo" role="img" aria-label="Cleaners washing glass windows" style="background:linear-gradient(135deg,#7a8086,#c8cbcf)"></div>
  <h3>WINDOW &amp; GLASS<br>CLEANING</h3>
  <p>Sparkling clean windows inside and out.</p>
  <span class="btn">VIEW MORE</span>
</div>
<div class="abs card" style="left:889px">
  <div class="photo" role="img" aria-label="Vacuuming a carpet floor" style="background:linear-gradient(135deg,#b7a99a,#8a7d72)"></div>
  <h3>FLOOR &amp; CARPET<br>CARE</h3>
  <p>Professional carpet cleaning, floor polishing, &amp; maintenance.</p>
  <span class="btn">VIEW MORE</span>
</div>
<div class="abs card" style="left:1133px">
  <div class="photo" role="img" aria-label="Industrial cleaning crew" style="background:linear-gradient(135deg,#c29a4a,#5c6a7a)"></div>
  <h3>INDUSTRIAL<br>CLEANING</h3>
  <p>Large-scale cleaning for factories.</p>
  <span class="btn">VIEW MORE</span>
</div>

<h2 class="abs section-title center why-title">WHY CHOOSE US?</h2>
<p class="abs center why-text">We provide environmentally friendly power washing services for commercial, industrial and residential<br>customers. Bright Lane operates new fleet of power washing trucks..</p>

<svg class="abs" style="left:89px;top:1765px" width="426" height="420" role="img" aria-label="Photo of a cleaner vacuuming an office">
  <defs><linearGradient id="g2" x1="0" y1="0" x2="1" y2="1"><stop offset="0" stop-color="#d9dbdd"/><stop offset=".6" stop-color="#6d7074"/><stop offset="1" stop-color="#3a3c3f"/></linearGradient></defs>
  <path fill="url(#g2)" d="M40,0 H386 A40,40 0 0 1 426,40 V266 A40,40 0 0 1 386,306 H363 A40,40 0 0 0 323,346 V380 A40,40 0 0 1 283,420 H40 A40,40 0 0 1 0,380 V40 A40,40 0 0 1 40,0 Z"/>
</svg>

<div class="abs why-list">
  <div class="why-item">OVER 10 YEARS OF EXPERIENCE</div>
  <div class="why-item" style="padding-top:24px">FULLY LICENSED AND CERTIFIED</div>
  <div class="why-item plain" style="padding-top:22px">FAMILY OPERATED BUSINESS</div>
  <div class="why-box">
    <h4>RECYCLING SOLUTIONS</h4>
    <p>We will not endanger the environment and your good company name by letting dirty wash water run freely into the storm drains on your property. Our trucks are equipped with a wastewater pickup and recycling system that allows us to filter and reuse the water that otherwise would end up in the nearest lake or pond.</p>
  </div>
  <div class="why-item">ENVIRONMENTALLY-FRIENDLY SOLUTIONS</div>
  <div class="why-item plain" style="padding-top:22px">NEW EQUIPMENT AND CLEAN ENGINES</div>
</div>

<p class="abs center fleet">Looking for truck fleet washing in Toronto or surrounding areas?<br>Bright Lane Mobile Wash team</p>

<h2 class="abs section-title areas-title">SERVICE AREAS</h2>
<p class="abs areas-text">Bright Lane Mobile Wash  offers high pressure cleaning services for the followings areas: (if you don't see your city listed, please contact us for further details)</p>

<svg class="abs" style="left:87px;top:2495px" width="1021" height="500" role="img" aria-label="Aerial photo of a city skyline at sunset">
  <defs><linearGradient id="g3" x1="0" y1="0" x2="1" y2="1"><stop offset="0" stop-color="#e9a57c"/><stop offset=".45" stop-color="#9a7a6e"/><stop offset="1" stop-color="#4a3b3a"/></linearGradient></defs>
  <path fill="url(#g3)" d="M613,0 H981 A40,40 0 0 1 1021,40 V355 A40,40 0 0 1 981,395 H920 A40,40 0 0 0 880,435 V460 A40,40 0 0 1 840,500 H40 A40,40 0 0 1 0,460 V182 A40,40 0 0 1 40,142 H533 A40,40 0 0 0 573,102 V40 A40,40 0 0 1 613,0 Z"/>
</svg>

<div class="abs areas">
  <ul style="width:212px;padding-left:38px"><li><svg width="15" height="15"><circle cx="7.5" cy="7.5" r="7.5" fill="#2ea84a"/><path d="M4 7.5l2.5 2.5 4.5-5" stroke="#fff" stroke-width="1.8" fill="none"/></svg>Brampton</li><li><svg width="15" height="15"><circle cx="7.5" cy="7.5" r="7.5" fill="#2ea84a"/><path d="M4 7.5l2.5 2.5 4.5-5" stroke="#fff" stroke-width="1.8" fill="none"/></svg>Burlington</li><li><svg width="15" height="15"><circle cx="7.5" cy="7.5" r="7.5" fill="#2ea84a"/><path d="M4 7.5l2.5 2.5 4.5-5" stroke="#fff" stroke-width="1.8" fill="none"/></svg>Don Mills</li><li><svg width="15" height="15"><circle cx="7.5" cy="7.5" r="7.5" fill="#2ea84a"/><path d="M4 7.5l2.5 2.5 4.5-5" stroke="#fff" stroke-width="1.8" fill="none"/></svg>Downsview</li><li><svg width="15" height="15"><circle cx="7.5" cy="7.5" r="7.5" fill="#2ea84a"/><path d="M4 7.5l2.5 2.5 4.5-5" stroke="#fff" stroke-width="1.8" fill="none"/></svg>East York</li></ul>
  <ul style="width:245px"><li><svg width="15" height="15"><circle cx="7.5" cy="7.5" r="7.5" fill="#2ea84a"/><path d="M4 7.5l2.5 2.5 4.5-5" stroke="#fff" stroke-width="1.8" fill="none"/></svg>Etobicoke</li><li><svg width="15" height="15"><circle cx="7.5" cy="7.5" r="7.5" fill="#2ea84a"/><path d="M4 7.5l2.5 2.5 4.5-5" stroke="#fff" stroke-width="1.8" fill="none"/></svg>Maple</li><li><svg width="15" height="15"><circle cx="7.5" cy="7.5" r="7.5" fill="#2ea84a"/><path d="M4 7.5l2.5 2.5 4.5-5" stroke="#fff" stroke-width="1.8" fill="none"/></svg>Markham</li><li><svg width="15" height="15"><circle cx="7.5" cy="7.5" r="7.5" fill="#2ea84a"/><path d="M4 7.5l2.5 2.5 4.5-5" stroke="#fff" stroke-width="1.8" fill="none"/></svg>Milton</li><li><svg width="15" height="15"><circle cx="7.5" cy="7.5" r="7.5" fill="#2ea84a"/><path d="M4 7.5l2.5 2.5 4.5-5" stroke="#fff" stroke-width="1.8" fill="none"/></svg>Mississauga</li></ul>
  <ul style="width:255px"><li><svg width="15" height="15"><circle cx="7.5" cy="7.5" r="7.5" fill="#2ea84a"/><path d="M4 7.5l2.5 2.5 4.5-5" stroke="#fff" stroke-width="1.8" fill="none"/></svg>North York</li><li><svg width="15" height="15"><circle cx="7.5" cy="7.5" r="7.5" fill="#2ea84a"/><path d="M4 7.5l2.5 2.5 4.5-5" stroke="#fff" stroke-width="1.8" fill="none"/></svg>Oakville</li><li><svg width="15" height="15"><circle cx="7.5" cy="7.5" r="7.5" fill="#2ea84a"/><path d="M4 7.5l2.5 2.5 4.5-5" stroke="#fff" stroke-width="1.8" fill="none"/></svg>Richmond Hill</li><li><svg width="15" height="15"><circle cx="7.5" cy="7.5" r="7.5" fill="#2ea84a"/><path d="M4 7.5l2.5 2.5 4.5-5" stroke="#fff" stroke-width="1.8" fill="none"/></svg>Scarborough</li><li><svg width="15" height="15"><circle cx="7.5" cy="7.5" r="7.5" fill="#2ea84a"/><path d="M4 7.5l2.5 2.5 4.5-5" stroke="#fff" stroke-width="1.8" fill="none"/></svg>Stouffville</li></ul>
  <ul style="width:230px"><li><svg width="15" height="15"><circle cx="7.5" cy="7.5" r="7.5" fill="#2ea84a"/><path d="M4 7.5l2.5 2.5 4.5-5" stroke="#fff" stroke-width="1.8" fill="none"/></svg>Toronto</li><li><svg width="15" height="15"><circle cx="7.5" cy="7.5" r="7.5" fill="#2ea84a"/><path d="M4 7.5l2.5 2.5 4.5-5" stroke="#fff" stroke-width="1.8" fill="none"/></svg>Thornhill</li><li><svg width="15" height="15"><circle cx="7.5" cy="7.5" r="7.5" fill="#2ea84a"/><path d="M4 7.5l2.5 2.5 4.5-5" stroke="#fff" stroke-width="1.8" fill="none"/></svg>Vaughan</li><li><svg width="15" height="15"><circle cx="7.5" cy="7.5" r="7.5" fill="#2ea84a"/><path d="M4 7.5l2.5 2.5 4.5-5" stroke="#fff" stroke-width="1.8" fill="none"/></svg>Willowdale</li><li><svg width="15" height="15"><circle cx="7.5" cy="7.5" r="7.5" fill="#2ea84a"/><path d="M4 7.5l2.5 2.5 4.5-5" stroke="#fff" stroke-width="1.8" fill="none"/></svg>York</li></ul>
</div>

<h2 class="abs section-title center quote-title">REQUEST A QUOTE</h2>
<p class="abs center quote-text">In just a few simple steps submit your quote request below and we will get back to you shortly!</p>

<div class="abs footer-bg"></div>

<div class="abs form">
  <div class="field" style="left:52px;top:44px;width:186px"><label>NAME*</label><div class="input">Enter name</div></div>
  <div class="field" style="left:250px;top:44px;width:185px"><label>EMAIL*</label><div class="input">Enter email</div></div>
  <div class="field" style="left:447px;top:44px;width:185px"><label>PHONE*</label><div class="input">Enter number</div></div>
  <div class="field" style="left:51px;top:115px;width:581px"><label>MESSAGE*</label><div class="input area">Type your message</div></div>
  <span class="abs btn submit">SUBMIT</span>
</div>

<div class="abs brand footer-brand"><span class="mark"></span>HARBOR<br>TIDY SQUAD</div>
<div class="abs fsocial" aria-label="Social links"><span></span><span></span><span></span></div>

<div class="abs fcol" style="left:444px;top:3915px">
  <h5>QUICK LINKS</h5>
  <div style="line-height:22px;font-size:11.5px">About Us<br>Why Harbor<br>Equipment &amp; Cleaners<br>Contact Us<br>Harbor Detailing<br>Harbor Washing<br>Site Map<br>Harbor Service</div>
</div>
<div class="abs fcol" style="left:668px;top:3920px;font-size:11.5px;line-height:18px">
  <h5>CONTACT US</h5>
  <b>PHONE</b><br>(555) 214-7730<br>
  <div style="height:12px"></div><b>EMAIL</b><br>harbortidysquad.com<br>
  <div style="height:12px"></div><b>ADDRESS</b><br>Some address line goes her<br>city name country
</div>
<div class="abs fcol" style="left:907px;top:3915px">
  <h5>WORKING HOURS</h5>
  <div class="hours" style="font-size:11.5px">
    <span>Mon</span><span>7.00 am–6:00 pm</span>
    <span>Tues</span><span>7.00 am–6:00 pm</span>
    <span>Wed</span><span>7.00 am–6:00 pm</span>
    <span>Thu</span><span>7.00 am–6:00 pm</span>
    <span>Fri</span><span>7.00 am–6:00 pm</span>
    <span>Sat</span><span>7.00 am–6:00 pm</span>
    <span>Sun</span><span>Closed</span>
  </div>
</div>

<div class="abs fline"></div>
<p class="abs center copy">© 2025 Harbor Tidy Squad. All Rights Reserved</p>

<div class="abs chat">
  <svg width="40" height="40"><path d="M11 13 h18 a3 3 0 0 1 3 3 v8 a3 3 0 0 1 -3 3 h-10 l-5 4 v-4 h-3 a3 3 0 0 1 -3 -3 v-8 a3 3 0 0 1 3 -3z" fill="#fff"/></svg>
</div>

</body>
</html>
```